Supplement website needs three beautiful graphic elements

We need three elements designed for our new website. They should be bright, attractive, and colorful. Feel free to incorporate relevant stock images into the design. If you do so, please include a link to the original graphics.

I have included some graphics from a competitor's website that I really love. Use them as a general guideline. I don't want you to copy these, but your designs should be inspired by them. Please do not use the same fonts for all the designs.

Please note: the winning designer for this project will be selected to work on the remaining graphics for our website, around 5-8 more banners.

The 3 items needed are:

1) "Proudly Made in the USA at a QRB Approved cGMP Facility" (230x100)

2) "Diet Pill Advice - Which Brand Is Right For Me? Find Out Now!" (345x145)

3) "100% Satisfaction Guaranteed Or Your Money Back!" (230x100)

Please make sure to look through the graphics I uploaded.  I love their color schemes, the rounded corners and friendly feel.  Font choices are very thoughtfully done.  I also like how some graphics bleed off the inner borders.  All of this should be taken into consideration when you are creating the designs.

```html
<!DOCTYPE html>
<html lang="en">
<head>
<meta charset="utf-8">
<title>Supplement Website Banners</title>
<link href="https://fonts.googleapis.com/css2?family=Rozha+One&family=Mulish:wght@700&family=Varela+Round&family=Cinzel:wght@500;700&family=Courgette&display=swap" rel="stylesheet">
<style>
  :root {
    --page: #ffffff;
    --ink: #111111;
    --lime-light: #eef5c8;
    --lime: #d6e89a;
    --btn-green: #3fae1f;
    --btn-light: #9fe040;
    --navy: #1d2a78;
    --red: #d4141c;
    --sky-top: #f7fbff;
    --sky-mid: #dbe9f8;
    --frame-grey: #9aa0a8;
    --night-deep: #1c1a45;
    --night-mid: #4a4a9c;
    --white: #ffffff;
  }
  html, body {
    margin: 0;
    width: 1200px;
    height: 848px;
    overflow: hidden;
    background: var(--page);
  }
  .canvas { position: relative; width: 1200px; height: 848px; }

  .banner {
    position: absolute;
    overflow: hidden;
    border-radius: 12px;
    box-shadow: 0 4px 6px rgba(0,0,0,0.35);
  }

  /* Diet pill advice */
  .advice {
    left: 349px; top: 198px; width: 501px; height: 210px;
    background: linear-gradient(160deg, var(--lime-light) 0%, var(--lime) 60%, #f4f8e4 100%);
  }
  .advice-art { position: absolute; inset: 0; }
  .advice-title {
    position: absolute; left: 22px; top: 14px; margin: 0;
    font-family: "Rozha One", serif; font-weight: 400;
    font-size: 50px; line-height: 1; color: var(--ink);
    letter-spacing: -0.5px;
  }
  .advice-sub {
    position: absolute; left: 34px; top: 74px; margin: 0;
    font-family: "Mulish", sans-serif; font-weight: 700;
    font-size: 20px; line-height: 24px; color: var(--ink);
  }
  .advice-sub span { display: block; padding-left: 44px; }
  .cta-label {
    position: absolute; left: 386px; top: 54px; width: 80px;
    font-family: "Varela Round", sans-serif; font-size: 19px;
    line-height: 21px; color: var(--white); text-align: center;
  }

  /* Made in USA */
  .made {
    left: 182px; top: 500px; width: 326px; height: 138px;
    border: 3px solid var(--frame-grey); box-sizing: border-box;
    background: linear-gradient(180deg, var(--sky-top) 0%, var(--sky-mid) 55%, #f3f8fd 100%);
  }
  .made-line {
    position: absolute; left: 0; width: 100%; margin: 0; text-align: center;
    font-family: "Cinzel", serif; font-weight: 500; color: var(--navy);
  }
  .made-line.top { top: 14px; font-size: 27px; }
  .made-line.mid { top: 56px; font-size: 27px; }
  .made-line.note {
    top: 98px; font-size: 13px; color: var(--red); font-weight: 500;
  }

  /* Guarantee */
  .guarantee {
    left: 685px; top: 496px; width: 333px; height: 144px;
    border: 2px solid #6c6a8a; box-sizing: border-box;
    background: radial-gradient(ellipse at 60% 60%, var(--night-mid) 0%, #2e2c6a 55%, var(--night-deep) 100%);
  }
  .gloss {
    position: absolute; right: -40px; top: -60px; width: 260px; height: 150px;
    background: linear-gradient(200deg, rgba(255,255,255,0.45), rgba(255,255,255,0.05));
    transform: rotate(-18deg); border-radius: 0 0 0 80px;
  }
  .g-text {
    position: absolute; margin: 0; color: var(--white);
    font-family: "Courgette", cursive; font-weight: 400;
  }
  .g-big { left: 22px; top: 14px; font-size: 54px; }
  .g-small { left: 176px; top: 14px; font-size: 22px; line-height: 32px; }
  .g-line { left: 0; width: 100%; text-align: center; top: 92px; font-size: 23px; }
</style>
</head>
<body>
<main class="canvas">

  <section class="banner advice">
    <svg class="advice-art" width="501" height="210" viewBox="0 0 501 210">
      <defs>
        <linearGradient id="pillTones" x1="0" y1="0" x2="1" y2="0">
          <stop offset="0" stop-color="#3aa84a"/>
          <stop offset="0.25" stop-color="#5b9be0"/>
          <stop offset="0.45" stop-color="#f2c340"/>
          <stop offset="0.7" stop-color="#f08a5c"/>
          <stop offset="1" stop-color="#fbe3e0"/>
        </linearGradient>
        <radialGradient id="ctaFill" cx="0.65" cy="0.3" r="0.8">
          <stop offset="0" stop-color="var(--btn-light)"/>
          <stop offset="1" stop-color="var(--btn-green)"/>
        </radialGradient>
      </defs>
      <path d="M0 150 C120 110 260 70 501 60 L501 210 L0 210 Z" fill="#ffffff" opacity="0.85"/>
      <path d="M0 120 C60 110 140 110 200 115 L380 135 L380 210 L0 210 Z" fill="url(#pillTones)" opacity="0.9" role="img" aria-label="Photo of colourful diet pills scattered on a white surface"/>
      <ellipse cx="432" cy="172" rx="44" ry="8" fill="#000" opacity="0.18"/>
      <path d="M430 28 C470 28 485 60 480 95 C474 130 450 150 430 150 C400 150 378 124 378 92 C378 55 398 28 430 28 Z" fill="url(#ctaFill)"/>
      <path d="M440 38 C462 44 474 64 472 86" stroke="#ffffff" stroke-width="4" fill="none" opacity="0.7" stroke-linecap="round"/>
    </svg>
    <h2 class="advice-title">Diet Pill Advice</h2>
    <p class="advice-sub">Which Brand Is Right<span>For Me?</span></p>
    <div class="cta-label">Find<br>Out<br>Now!</div>
  </section>

  <section class="banner made">
    <p class="made-line top">Proudly Made</p>
    <p class="made-line mid">in the USA</p>
    <p class="made-line note">AT A QRB APPROVED cGMP FACILITY</p>
  </section>

  <section class="banner guarantee">
    <div class="gloss"></div>
    <p class="g-text g-big">100%</p>
    <p class="g-text g-small">Satisfaction<br>Guaranteed</p>
    <p class="g-text g-line">Or Your Money Back!!</p>
  </section>

</main>
</body>
</html>
```